Wedding Invitation : Who helps to design a chic wedding card?

We need a chic invitation design for our wedding invitations.

FRONT

- Name logo : Mirte & Koen
- Wedding date : zaterdag 9 juli 2022
- Quote : forever starts here

BACK

- Wij geven elkaar het ja-woord op zaterdag 9 juli 2022
Translation: We’ll say yes on Saturday 9th of July 2022 in the church of Landskouter
- Timeline with icons:

o JAWOORD (Translation: We say yes)
o 15u00

o RECEPTIE (Translation: Reception)
o 18u30

o DINER (Translation: Dinner)
o 19u30
o Feestzaal Volderhof (Location)

o FEEST (Translation: Dinner)
o 21u30

- Locations:

o Icon of a church:
Landskouter
o Icon of a location:
Feestzaal Volderhof
Kapelmeester Drovenstraat 47B
9820 Merelbeke

- RSVP Gelieve jouw aanwezigheid te bevestigen voor 29 mei 2022
(Translation: Please confirm before 29th of May 2022)

STYLE:

- Rosé gold relief press symbols
- Font style : handwritten or serif name (eg. playfair display)
- Font style: description in a more minimalistic font
- Cards will be in craft or ivory white, text will be in rosé gold relief press or black print

FORMAT
American format (229mm W x 114 mm H)

Target Market(s)

People 25-40 years old

Industry/Entity Type

Wedding / Event

Font styles to use
Serif
Sans Serif
Script

Colors

Designer to choose colors to be used in the design.

Requirements
Must have
• Name logo
Nice to have
• Minimalistic animation / icons
Should not have
• Jungle prints

```html
<!DOCTYPE html>
<html lang="nl">
<head>
<meta charset="utf-8">
<title>Mirte &amp; Koen – zaterdag 9 juli 2022</title>
<link rel="stylesheet" href="https://fonts.googleapis.com/css2?family=Josefin+Sans:wght@400;700&family=Pinyon+Script&display=swap">
<style>
  :root {
    --backdrop: #ece7e1;
    --card: #fdfdfc;
    --rose-gold: #eaa48f;
    --rose-gold-light: #f6cdbf;
    --ink: #161616;
  }
  html, body {
    margin: 0;
    width: 1200px;
    height: 961px;
    overflow: hidden;
    background: var(--backdrop);
  }
  .invitation-front {
    position: absolute;
    left: 100px;
    top: 232px;
    width: 1000px;
    height: 497px;
    background: var(--card);
    box-shadow: 0 6px 24px rgba(60, 40, 20, 0.12);
  }
  .frame {
    position: absolute;
    left: 80px;
    top: 50px;
    width: 850px;
    height: 370px;
    border: 1px solid var(--rose-gold);
    box-sizing: border-box;
  }
  .frame::after {
    content: "";
    position: absolute;
    inset: 4px;
    border: 1px solid var(--rose-gold-light);
  }
  .monogram {
    position: absolute;
    left: 405px;
    top: 150px;
    width: 150px;
    height: 100px;
    border-radius: 6px;
    background: linear-gradient(135deg, var(--rose-gold), var(--rose-gold-light));
    opacity: 0.55;
  }
  .couple-names {
    position: absolute;
    left: 0;
    width: 960px;
    top: 282px;
    margin: 0;
    text-align: center;
    font-family: "Josefin Sans", sans-serif;
    font-weight: 700;
    font-size: 34px;
    letter-spacing: 4px;
    color: var(--ink);
  }
  .wedding-date {
    position: absolute;
    left: 0;
    width: 960px;
    top: 340px;
    margin: 0;
    text-align: center;
    font-family: "Josefin Sans", sans-serif;
    font-weight: 400;
    font-size: 20px;
    letter-spacing: 4px;
    color: var(--ink);
  }
  .quote {
    position: absolute;
    right: 70px;
    top: 436px;
    margin: 0;
    font-family: "Pinyon Script", cursive;
    font-size: 26px;
    color: var(--ink);
  }
</style>
</head>
<body>
  <section class="invitation-front">
    <div class="frame"></div>
    <div class="monogram" role="img" aria-label="Rose gold script monogram of the couple's initials"></div>
    <h1 class="couple-names">MIRTE &amp; KOEN</h1>
    <p class="wedding-date">zaterdag 9 juli 2022</p>
    <p class="quote">forever starts here...</p>
  </section>
</body>
</html>
```